Law firm Seeks Modern and Engaging Site Redesign

Law firm seeks a new web site. Should be modern, but retaining existing logo. Needs to include contact section, professional bio, services offered, and contact information.

The site should be modern, responsive, and able to be SEO optimized.

The finished product should be coded in a Wordpress site, which I will provide. I can work with other platforms, including Wix, but WP is preferred.

Note the current site is https://www.tallowfieldlaw.example/#/home

Target Market(s)

Family Law Practice

Industry/Entity Type

Legal

Coding

Coded - Design and coding required

Number of Pages Required

4 page

Font styles to use
Sans Serif

Requirements
Must have
• Service description
Bio pages for partners
Contact Form
Awards/Publication page

```html
<!DOCTYPE html>
<html lang="en">
<head>
<meta charset="utf-8">
<title>About Us – Tallowfield Attorneys</title>
<link rel="stylesheet" href="https://fonts.googleapis.com/css2?family=Open+Sans:wght@400;600;700&family=Poppins:wght@400;500&display=swap">
<style>
:root{
  --brand:#0450b4;
  --brand-dark:#1f4fa8;
  --hero:#2b4a74;
  --hero-light:#3d5e8b;
  --ink:#1b1b1b;
  --muted:#6b6b6b;
  --rule:#e8e8e8;
  --footer:#1c1c1c;
  --footer-text:#bdbdbd;
  --white:#fff;
}
*{margin:0;padding:0;box-sizing:border-box}
html,body{width:736px;height:1200px;overflow:hidden;background:var(--white)}
body{position:relative;font-family:"Open Sans",sans-serif;color:var(--ink)}
.abs{position:absolute}

/* header */
.site-header{position:absolute;left:0;top:0;width:736px;height:44px;background:var(--white)}
.brand-name{position:absolute;left:140px;top:13px;font-family:"Open Sans",sans-serif;font-size:12px;font-weight:400;color:var(--brand-dark)}
.main-nav a{position:absolute;top:18px;font-size:6.3px;letter-spacing:1.6px;color:var(--ink);text-decoration:none;font-weight:400}
.main-nav a.is-active{color:var(--brand-dark);font-weight:700}

/* hero */
.page-hero{position:absolute;left:0;top:44px;width:736px;height:124px;background:linear-gradient(100deg,var(--hero) 0%,var(--hero-light) 50%,var(--hero) 100%)}
.page-hero h1{position:absolute;left:141px;top:44px;font-size:25px;font-weight:600;color:var(--white)}

/* team */
.team-member{position:absolute;left:140px;width:456px}
.member-photo{position:absolute;left:0;top:0;width:80px;height:77px;border-radius:26px 30px 24px 22px / 22px 26px 32px 26px;background:linear-gradient(135deg,#a9adb5,#4a4f5c)}
.member-photo.placeholder{background:var(--brand)}
.member-name{position:absolute;left:97px;top:1px;font-size:10px;font-weight:400}
.member-email{position:absolute;right:0;top:4px;font-size:6.4px}
.member-email a{color:var(--brand-dark);text-decoration:none}
.member-bio{position:absolute;left:97px;top:15px;width:359px;font-size:7.3px;line-height:13.2px;overflow:hidden}
.read-more{position:absolute;left:97px;font-size:6.6px;font-weight:700;color:var(--brand-dark);text-decoration:none}
.divider{position:absolute;left:140px;width:456px;height:1px;background:var(--rule)}

/* contact */
.contact-band{position:absolute;left:0;top:636px;width:362px;height:361px;background:var(--brand)}
.eyebrow{position:absolute;left:140px;top:36px;font-family:"Poppins",sans-serif;font-size:5.4px;font-weight:500;letter-spacing:1.6px;color:var(--white)}
.contact-band h2{position:absolute;left:140px;top:45px;font-size:19.5px;font-weight:400;color:var(--white)}
.field{position:absolute;left:141px;width:175px;height:19px;background:var(--white);font-family:"Poppins",sans-serif;font-size:6.2px;color:#8a8a8a;padding:6px 6px}
.field.select::after{content:"";position:absolute;right:7px;top:7.5px;border-left:2.5px solid transparent;border-right:2.5px solid transparent;border-top:4px solid #111}
.field.message{height:43px}
.submit-btn{position:absolute;left:141px;top:244px;width:62px;height:24px;border:1.5px solid var(--white);color:var(--white);font-family:"Poppins",sans-serif;font-size:7px;font-weight:500;text-align:center;line-height:21px}
.map{position:absolute;left:362px;top:636px;width:374px;height:361px;background:linear-gradient(135deg,#eef0f2 0%,#e3ece0 45%,#bcd6f2 70%,#edf0f2 100%)}

/* footer */
.site-footer{position:absolute;left:0;top:997px;width:736px;height:203px;background:var(--footer);font-family:"Poppins",sans-serif;color:var(--footer-text)}
.col-rule{position:absolute;top:0;width:1px;height:151px;background:#2a2a2a}
.foot-rule{position:absolute;left:0;top:151px;width:736px;height:1px;background:#2a2a2a}
.info-label{position:absolute;left:156px;font-size:6.4px;font-weight:500;color:var(--white)}
.info-value{position:absolute;left:156px;font-size:6.2px}
.info-icon{position:absolute;left:141px;width:9px;height:9px}
.footer-brand{position:absolute;left:305px;top:20px;font-family:"Open Sans",sans-serif;font-size:11px;color:#8a8a8a}
.footer-about{position:absolute;left:305px;top:48px;width:140px;font-size:6.3px;line-height:13.2px}
.footer-about a{color:var(--brand);font-weight:500;text-decoration:none}
.footer-links a{position:absolute;right:141px;font-size:6.3px;color:var(--footer-text);text-decoration:none}
.copyright{position:absolute;left:0;width:736px;top:174px;text-align:center;font-size:6.2px}
</style>
</head>
<body>

<header class="site-header">
  <div class="brand-name">Tallowfield</div>
  <nav class="main-nav">
    <a href="#" style="left:380px">HOME</a>
    <a href="#" class="is-active" style="left:429px">ABOUT US</a>
    <a href="#" style="left:496px">SERVICES</a>
    <a href="#" style="left:559px">CONTACT</a>
  </nav>
</header>

<section class="page-hero" role="img" aria-label="Photo of classical stone column bases tinted blue">
  <h1>About Us</h1>
</section>

<article class="team-member" style="top:190px">
  <div class="member-photo" role="img" aria-label="Portrait of Martin L. Tallow in a suit"></div>
  <h3 class="member-name">Martin L. Tallow</h3>
  <p class="member-email">email : <a href="#">mtallow@tallowfieldlaw.example</a></p>
  <p class="member-bio" style="height:52.8px">Martin L. Tallow practices in the area of family law, specializing in high conflict matters relating to divorce, custody, equitable distribution, and complex financial issues.&nbsp; Additionally, Mr. Tallow specializes in DCPP (formerly known as DYFS)-related litigation and DCPP defense matters, as well as domestic violence proceedings.&nbsp; An established trial attorney and litigator, Mr. Tallow is certified by the State Supreme Court.</p>
  <a class="read-more" href="#" style="top:70px">Read More</a>
</article>
<div class="divider" style="top:282px"></div>

<article class="team-member" style="top:300px">
  <div class="member-photo" role="img" aria-label="Portrait of Owen T. Hartwell seated in an office"></div>
  <h3 class="member-name">Owen T. Hartwell</h3>
  <p class="member-email">email : <a href="#">ohartwell@tallowfieldlaw.example</a></p>
  <p class="member-bio">Owen T. Hartwell is one of the founding partners of the firm. Mr. Hartwell's primary concentration is in the areas of matrimonial, family law, appellate work, juvenile delinquency, criminal, municipal court, residential real estate transactions and wills and estates.</p>
  <a class="read-more" href="#" style="top:60px">Read More</a>
</article>
<div class="divider" style="top:395px"></div>

<article class="team-member" style="top:414px">
  <div class="member-photo" role="img" aria-label="Portrait of Nora L. Abernath outdoors"></div>
  <h3 class="member-name">Nora L. Abernath</h3>
  <p class="member-email">email : <a href="#">nabernath@tallowfieldlaw.example</a></p>
  <p class="member-bio">Nora Abernath has been an associate at Tallowfield since 2016. In private practice, Ms. Abernath focuses her practice on family and divorce law, which includes child custody, child and spousal support, equitable distribution. She is a member of the Westbrook County Bar Association and the State Bar Association. Ms. Abernath also volunteers as a member of the Early Settlement Panel.</p>
  <a class="read-more" href="#" style="top:72px">Read More</a>
</article>
<div class="divider" style="top:507px"></div>

<article class="team-member" style="top:526px">
  <div class="member-photo placeholder" role="img" aria-label="Portrait placeholder for Lucia M. Veranti"></div>
  <h3 class="member-name">Lucia M. Veranti</h3>
  <p class="member-email">email : <a href="#">lveranti@tallowfieldlaw.example</a></p>
  <p class="member-bio">Lucia M. Veranti, Esq. (“Lucy”) is a skilled and experienced litigator specializing in all facets of family and matrimonial law. Ms. Veranti’s practice includes marital dissolution and non-dissolution proceedings, child custody and support matters, drafting and negotiation of pre-nuptial agreements, and all aspects of pre and post-judgment litigation.</p>
  <a class="read-more" href="#" style="top:72px">Read More</a>
</article>

<section class="contact-band">
  <p class="eyebrow">CONTACT US</p>
  <h2>For more Enquery</h2>
  <div class="field" style="top:81px">Name</div>
  <div class="field" style="top:107px">Email</div>
  <div class="field" style="top:133px">Phone Number</div>
  <div class="field select" style="top:158px">Practice Area</div>
  <div class="field message" style="top:184px">Message</div>
  <div class="submit-btn">Submit</div>
</section>
<div class="map" role="img" aria-label="Street map showing the office location beside a river"></div>

<footer class="site-footer">
  <svg class="info-icon" style="top:20px" viewBox="0 0 10 10"><path d="M1 4 5 1 9 4V9H1Z" fill="#1f5fcc"/><path d="M1 4 5 7 9 4" fill="none" stroke="#1c1c1c" stroke-width=".8"/></svg>
  <span class="info-label" style="top:18px">Email</span>
  <span class="info-value" style="top:30px">info@tallowfieldlaw.example</span>
  <svg class="info-icon" style="top:43px" viewBox="0 0 10 10"><path d="M2 2c1-1 2 0 2 1L3 4c0 1 2 3 3 3l1-1c1 0 2 1 1 2-2 2-7-3-6-6Z" fill="#1f5fcc"/></svg>
  <span class="info-label" style="top:41px">Phone</span>
  <span class="info-value" style="top:53px">(555) 014-2290</span>
  <svg class="info-icon" style="top:66px" viewBox="0 0 10 10"><rect x="1" y="3" width="8" height="6" fill="#1f5fcc"/><rect x="3" y="1" width="4" height="3" fill="#1f5fcc"/></svg>
  <span class="info-label" style="top:64px">Fax</span>
  <span class="info-value" style="top:76px">(555) 014-2290</span>
  <svg class="info-icon" style="top:89px" viewBox="0 0 10 10"><path d="M5 0a3 3 0 0 1 3 3c0 2-3 7-3 7S2 5 2 3a3 3 0 0 1 3-3Z" fill="#1f5fcc"/></svg>
  <span class="info-label" style="top:88px">Address</span>
  <span class="info-value" style="top:100px">Tallowfield LLC</span>
  <span class="info-value" style="top:112px">48 Linden Court Suite 210</span>
  <span class="info-value" style="top:124px">Westbrook, NJ 07990</span>

  <div class="col-rule" style="left:284px"></div>
  <div class="col-rule" style="left:452px"></div>

  <div class="footer-brand">Tallowfield</div>
  <p class="footer-about">The law firm of Tallowfield, LLC is based in Westbrook County, conveniently located in Westbrook at 48 Linden Court. <a href="#">Read More</a></p>

  <nav class="footer-links">
    <a href="#" style="top:18px">Home</a>
    <a href="#" style="top:34px">About Us</a>
    <a href="#" style="top:49px">Services</a>
    <a href="#" style="top:65px">Contact Us</a>
  </nav>

  <div class="foot-rule"></div>
  <p class="copyright">© copyright 2020 by Tallowfield</p>
</footer>

</body>
</html>
```